EPIC, awesome, creative business card needed - get involved!

I'm launching a boutique, exclusive Property Management real estate agency in Sydney early next year.
The name of the agency will be called "Silver Oak Lane" - it's a play on "follow the yellow brick road" to wealth. The Silver Oak Lane signifies wealth through property investment.
My business will offer management of investment properties (ie Property Management).
The difference with Silver Oak Lane and other agencies is the business will be run by one of Australia's leading property investment experts, and also one of Australia's leading property managers.
It will be exclusively for high net worth properties and individuals, so the business card needs to be extremely sharp, slick and relatively simple.
The information I want on the card is as follows
Marcus Fenwick - Director
M: 0471 926 154
P: 9637 0518
E: marcus@silveroaklane.net.au
W: silveroaklane.net.au
I'm happy with the red from the logo, black - no yellows or funky colors. I want this to be a super corporate and slick business card to match the high end nature of the business.
Good luck everyone, and please ask questions for clarification.

```html
<!DOCTYPE html>
<html lang="en">
<head>
<meta charset="utf-8">
<title>Silver Oak Lane – Business Card</title>
<link rel="stylesheet" href="https://fonts.googleapis.com/css2?family=Jura:wght@500;700&display=swap">
<style>
  :root {
    --page: #ffffff;
    --frame: #9a9a9a;
    --card-top: #545456;
    --card-bottom: #231f20;
    --brand-red: #c00000;
    --ink-light: #ffffff;
  }
  * { margin: 0; padding: 0; box-sizing: border-box; }
  html, body {
    width: 1200px;
    height: 899px;
    overflow: hidden;
    background: var(--page);
    font-family: "Jura", sans-serif;
  }
  .sheet {
    position: relative;
    width: 1200px;
    height: 899px;
    border: 1px solid var(--frame);
  }
  .card {
    position: absolute;
    left: 231px;
    width: 739px;
    height: 406px;
    background: linear-gradient(to bottom, var(--card-top), var(--card-bottom));
  }
  .card--front { top: 27px; }
  .card--back { top: 465px; }

  .wordmark {
    position: absolute;
    display: flex;
    align-items: flex-start;
    gap: 12px;
    color: var(--ink-light);
    font-weight: 700;
    text-transform: uppercase;
    line-height: 1.02;
  }
  .wordmark__square {
    flex: none;
    width: 22px;
    height: 22px;
  }
  .wordmark__name span { display: block; }

  .card--front .wordmark {
    left: 290px;
    top: 122px;
    font-size: 38px;
  }
  .card--front .wordmark__square { background: var(--brand-red); margin-top: 8px; }

  .card--back .wordmark {
    left: 110px;
    top: 132px;
    font-size: 30px;
  }
  .card--back .wordmark__square { background: var(--ink-light); margin-top: 6px; width: 18px; height: 18px; }

  .contact {
    position: absolute;
    left: 305px;
    top: 124px;
    list-style: none;
    color: var(--ink-light);
    font-size: 23px;
    font-weight: 500;
    letter-spacing: 0.3px;
  }
  .contact li { height: 33.5px; line-height: 33.5px; white-space: nowrap; }
</style>
</head>
<body>
  <main class="sheet">
    <section class="card card--front" aria-label="Card front">
      <div class="wordmark">
        <span class="wordmark__square"></span>
        <p class="wordmark__name"><span>Silver</span><span>Oak</span><span>Lane</span></p>
      </div>
    </section>

    <section class="card card--back" aria-label="Card back">
      <div class="wordmark">
        <span class="wordmark__square"></span>
        <p class="wordmark__name"><span>Silver</span><span>Oak</span><span>Lane</span></p>
      </div>
      <ul class="contact">
        <li class="contact__name">Marcus Fenwick - Director</li>
        <li>M: 0471 926 154</li>
        <li>P: 9637 0518</li>
        <li>E: marcus@silveroaklane.net.au</li>
        <li>W: silveroaklane.net.au</li>
      </ul>
    </section>
  </main>
</body>
</html>
```